Driving School Business card design

Hi, we are starting a new business (Driving School) and would like your help with our business card design.
We are located in Adelaide SA.
Our aim is to help young people achieve best possible results by promoting safe and stress free driving.

Name of our school is "Velmira" which means best or most favorable.

Hope there is someone out there in wonderful world of design who can think outside of square and give us recognizable/ unique business card design.

Target Market(s)

16+

Industry/Entity Type

Business

Contact Information for Business Card

Name of our business is "Velmira driver training"
Our idea is to make letter "L' in Velmira more distinct (noticeable) by different color or font, so it gets associated with learner driver.
We like combination of white, dark gray and yellow but do not limit our self to that.
Reverse side of our card would have to incorporate writing space for date and time of the next lesson.

Requirements
Must have
• Business name: Velmira driver training
• Owner/ instructor name
• Mobile no:
• Chatterloop logo
Should not have
• Anything Not associated with driving

```html
<!DOCTYPE html>
<html lang="en">
<head>
<meta charset="utf-8">
<title>Velmira Driver Training – Business Card</title>
<link rel="stylesheet" href="https://fonts.googleapis.com/css2?family=Saira+Condensed:wght@400;600;700&display=swap">
<style>
  :root {
    --backdrop: #6f7a8c;
    --card-gray: #58585a;
    --ink-gray: #5b5b5d;
    --signal-yellow: #f2ea3a;
    --road-dark: #1d2220;
    --road-yellow: #d9a722;
    --paper: #ffffff;
    --paper-shade: #ededed;
    --text-light: #f1f1f1;
  }
  * { margin: 0; padding: 0; box-sizing: border-box; }
  html, body { width: 1200px; height: 1200px; overflow: hidden; }
  body {
    background: var(--backdrop);
    font-family: "Saira Condensed", "Arial Narrow", sans-serif;
    position: relative;
  }
  .card {
    position: absolute;
    left: 150px;
    width: 900px;
    height: 514px;
    overflow: hidden;
    box-shadow: 0 8px 24px rgba(0,0,0,.25);
  }
  .card--back { top: 60px; background: linear-gradient(120deg, var(--paper) 55%, var(--paper-shade)); }
  .card--front { top: 626px; background: var(--card-gray); }
  .road-art { position: absolute; inset: 0; width: 900px; height: 514px; }

  /* Front side */
  .brand { position: absolute; right: 70px; text-align: right; }
  .brand--front { top: 48px; }
  .brand__name {
    display: inline-flex; align-items: center; gap: 12px;
    font-weight: 700; font-size: 60px; line-height: 1; letter-spacing: 4px;
    color: var(--signal-yellow);
  }
  .brand__mark { width: 26px; height: 26px; background: currentColor; }
  .brand__tagline { font-weight: 600; font-size: 48px; line-height: 1.05; color: var(--signal-yellow); }

  .holder { position: absolute; right: 70px; top: 228px; text-align: right; }
  .holder__name { font-weight: 700; font-size: 52px; line-height: 1; color: var(--signal-yellow); }
  .holder__role { font-weight: 400; font-size: 30px; color: var(--text-light); letter-spacing: 1px; }

  .contacts { position: absolute; right: 70px; top: 350px; list-style: none; text-align: right; }
  .contacts__item {
    display: flex; justify-content: flex-end; align-items: center; gap: 14px;
    font-size: 28px; line-height: 44px; color: var(--text-light); letter-spacing: 1px;
    white-space: nowrap;
  }
  .contacts__item--social { font-size: 26px; letter-spacing: 2px; gap: 12px; }
  .contacts__icon { width: 26px; height: 26px; background: var(--signal-yellow); border-radius: 3px; flex: none; }
  .contacts__network { font-size: 20px; font-weight: 600; letter-spacing: 0; color: var(--signal-yellow); }

  /* Back side */
  .booking { position: absolute; left: 56px; top: 96px; width: 520px; list-style: none; }
  .booking__row {
    display: flex; align-items: baseline; gap: 8px;
    font-size: 26px; color: var(--ink-gray); height: 64px;
  }
  .booking__label { flex: none; }
  .booking__fill { flex: 1; border-bottom: 2px dotted var(--ink-gray); transform: translateY(-6px); }
  .brand--back { right: auto; left: 290px; bottom: 40px; }
  .brand--back .brand__name, .brand--back .brand__tagline { color: var(--ink-gray); }
  .brand--back .brand__name { font-size: 54px; }
  .brand--back .brand__tagline { font-size: 42px; }
</style>
</head>
<body>

<section class="card card--back" aria-label="Back of card: next lesson booking">
  <svg class="road-art" viewBox="0 0 900 514">
    <defs>
      <linearGradient id="roadBack" x1="0" y1="0" x2="1" y2="0">
        <stop offset="0" stop-color="#1d2220"/>
        <stop offset=".35" stop-color="#d9a722"/>
        <stop offset=".5" stop-color="#1d2220"/>
        <stop offset=".75" stop-color="#d9a722"/>
        <stop offset="1" stop-color="#1d2220"/>
      </linearGradient>
    </defs>
    <polygon points="600,0 900,0 900,514 710,514" fill="url(#roadBack)" role="img" aria-label="Photo of road surface with double yellow lines"/>
    <line x1="600" y1="0" x2="710" y2="514" stroke="var(--signal-yellow)" stroke-width="5"/>
  </svg>

  <ul class="booking">
    <li class="booking__row"><span class="booking__label">Date:</span><span class="booking__fill"></span><span class="booking__label">Time:</span><span class="booking__fill"></span></li>
    <li class="booking__row"><span class="booking__label">Date:</span><span class="booking__fill"></span><span class="booking__label">Time:</span><span class="booking__fill"></span></li>
    <li class="booking__row"><span class="booking__label">Date:</span><span class="booking__fill"></span><span class="booking__label">Time:</span><span class="booking__fill"></span></li>
  </ul>

  <div class="brand brand--back">
    <div class="brand__name"><span class="brand__mark"></span>VELMIRA</div>
    <div class="brand__tagline">Driver Training</div>
  </div>
</section>

<section class="card card--front" aria-label="Front of card">
  <svg class="road-art" viewBox="0 0 900 514">
    <defs>
      <linearGradient id="roadFront" x1="0" y1="0" x2="1" y2="0">
        <stop offset="0" stop-color="#1d2220"/>
        <stop offset=".2" stop-color="#d9a722"/>
        <stop offset=".38" stop-color="#1d2220"/>
        <stop offset=".6" stop-color="#d9a722"/>
        <stop offset="1" stop-color="#1d2220"/>
      </linearGradient>
    </defs>
    <polygon points="0,0 210,0 420,514 0,514" fill="url(#roadFront)" role="img" aria-label="Photo of road surface with double yellow lines"/>
    <line x1="210" y1="0" x2="420" y2="514" stroke="var(--signal-yellow)" stroke-width="5"/>
  </svg>

  <div class="brand brand--front">
    <div class="brand__name"><span class="brand__mark"></span>VELMIRA</div>
    <div class="brand__tagline">Driver Training</div>
  </div>

  <div class="holder">
    <div class="holder__name">Marcus Hale</div>
    <div class="holder__role">Owner/ instructor</div>
  </div>

  <ul class="contacts">
    <li class="contacts__item">+61 400 555 012
      <svg class="contacts__icon" viewBox="0 0 26 26" aria-label="Mobile"><rect x="8" y="4" width="10" height="18" rx="2" fill="none" stroke="#58585a" stroke-width="2"/><circle cx="13" cy="19" r="1" fill="#58585a"/></svg>
    </li>
    <li class="contacts__item">www.velmiradrivertraining.com
      <svg class="contacts__icon" viewBox="0 0 26 26" aria-label="Web and email"><rect x="4" y="7" width="18" height="12" fill="none" stroke="#58585a" stroke-width="2"/><polyline points="4,7 13,14 22,7" fill="none" stroke="#58585a" stroke-width="2"/></svg>
    </li>
    <li class="contacts__item contacts__item--social">Velmira Driver Training
      <span class="contacts__network">Chatterloop</span>
    </li>
  </ul>
</section>

</body>
</html>
```